Bref créative
Valmira
Home Staging
Professional
Nora Pitt
Certified Staging Professional
Eastern Suburbs & Inner Sydney
info@valmira.com.au
www.valmira.com.au
Perhaps have the Logo on the front & the contact details on the back? Play around and see what looks best.
If more info looks good, try adding my services:
Open house staging
Interior Organisation
Move in service

```html
<!DOCTYPE html>
<html lang="en">
<head>
<meta charset="utf-8">
<title>Valmira Home Staging – Stationery</title>
<link rel="stylesheet" href="https://fonts.googleapis.com/css2?family=Didact+Gothic&family=Allura&display=swap">
<style>
  :root {
    --paper: #ffffff;
    --ink: #5d6166;
    --card-dark: #57595c;
    --brand-blue: #2c8fd6;
    --brand-green: #8cc63f;
    --line: #9a9a9a;
    --text-light: #f2f2f2;
  }
  * { margin: 0; padding: 0; box-sizing: border-box; }
  html, body { width: 1200px; height: 787px; overflow: hidden; background: var(--paper); }
  body { position: relative; font-family: "Didact Gothic", "Century Gothic", sans-serif; color: var(--ink); }

  .letterhead {
    position: absolute; left: 43px; top: -2px; width: 1114px; height: 194px;
    border: 1.5px solid var(--line); border-top: none; background: var(--paper);
  }
  .brand { position: absolute; display: flex; align-items: center; gap: 8px; }
  .brand-mark { border-radius: 50%; background: var(--brand-green); flex: none; }
  .brand-name { color: var(--brand-blue); font-family: "Didact Gothic", "Century Gothic", sans-serif; line-height: 1; }

  .letterhead .brand { left: 420px; top: 74px; }
  .letterhead .brand-mark { width: 18px; height: 18px; }
  .letterhead .brand-name { font-size: 38px; }

  .letterhead-contact { position: absolute; left: 624px; top: 72px; font-size: 18px; letter-spacing: 1.5px; line-height: 25px; }
  .letterhead-contact .area { font-size: 11px; letter-spacing: 1px; line-height: 20px; }
  .accent-band {
    position: absolute; left: 660px; top: 146px; width: 230px; height: 10px;
    background: linear-gradient(90deg, var(--brand-green), var(--brand-blue) 45%, var(--card-dark));
  }

  .card { position: absolute; top: 271px; width: 449px; height: 240px; }
  .card svg.shape { position: absolute; inset: 0; }
  .card-front { left: 113px; }
  .card-front .brand { left: 258px; top: 144px; }
  .card-front .brand-mark { width: 14px; height: 14px; }
  .card-front .brand-name { font-size: 30px; }

  .card-back { left: 600px; color: var(--text-light); }
  .card-back .edge {
    position: absolute; left: 0; top: 0; width: 10px; height: 240px;
    background: linear-gradient(180deg, var(--brand-green), var(--card-dark) 50%, var(--brand-blue));
  }
  .card-back .details { position: absolute; left: 0; width: 100%; top: 70px; text-align: center; }
  .card-back .name { font-family: "Allura", cursive; font-size: 40px; letter-spacing: 2px; line-height: 1; }
  .card-back .role { margin-top: 14px; font-size: 10px; letter-spacing: 1.5px; text-transform: uppercase; }
  .card-back .phone, .card-back .email { font-size: 17px; letter-spacing: 1.5px; line-height: 21px; }
  .card-back .phone { margin-top: 4px; }
  .card-back .web { position: absolute; left: 0; width: 100%; top: 212px; text-align: center; font-size: 11px; letter-spacing: 1px; color: var(--brand-green); }

  .logo-large { left: 806px; top: 680px; }
  .logo-large .brand-mark { width: 30px; height: 30px; }
  .logo-large .brand-name { font-size: 58px; }
</style>
</head>
<body>
  <section class="letterhead">
    <div class="brand">
      <span class="brand-mark"></span>
      <span class="brand-name">valmira</span>
    </div>
    <div class="letterhead-contact">
      <p>0412 555 018</p>
      <p>info@valmira.com.au</p>
      <p class="area">Eastern Suburbs &amp; Inner Sydney</p>
    </div>
    <div class="accent-band" role="img" aria-label="Decorative multicolour accent stripe"></div>
  </section>

  <section class="card card-front">
    <svg class="shape" width="449" height="240" viewBox="0 0 449 240">
      <path d="M1 240 V80 C40 10 200 2 449 2 V240 Z" fill="var(--paper)" stroke="var(--line)" stroke-width="1.5"/>
    </svg>
    <div class="brand">
      <span class="brand-mark"></span>
      <span class="brand-name">valmira</span>
    </div>
  </section>

  <section class="card card-back">
    <svg class="shape" width="449" height="240" viewBox="0 0 449 240">
      <path d="M0 0 H250 C360 0 420 30 449 80 V240 H0 Z" fill="var(--card-dark)"/>
    </svg>
    <div class="edge" role="img" aria-label="Decorative multicolour edge stripe"></div>
    <div class="details">
      <p class="name">Nora Pitt</p>
      <p class="role">Certified Staging Professional</p>
      <p class="phone">0412 555 018</p>
      <p class="email">info@valmira.com.au</p>
    </div>
    <p class="web">www.valmira.com.au</p>
  </section>

  <div class="brand logo-large">
    <span class="brand-mark"></span>
    <span class="brand-name">valmira</span>
  </div>
</body>
</html>
```